Business cards - KESTO Roofing & Siding

We need simple business cards made up for our Roofing & Siding business based in Calgary Alberta.
The logo on one side of the card and potentially our slogan "Built with trust, verified by time".
The other side could have:
-A small logo
-Rep name:
-Rep cell phone:
-Rep email:
-Office phone: 403-386-2049
-Website: PrairieShinglePros.com

We would like to incorporate the colours from our logo, especially the lite blue on the jpeg file. I have attached the ai file and jpeg file. We like the colours better on the jpeg file.

I do not require a money back guarantee

```html
<!DOCTYPE html>
<html lang="en">
<head>
<meta charset="utf-8">
<title>KESTO Roofing &amp; Siding – Business Cards</title>
<link href="https://fonts.googleapis.com/css2?family=Montserrat:wght@400;500;700&display=swap" rel="stylesheet">
<style>
  :root {
    --page-bg: #e9eaec;
    --card-white: #ffffff;
    --card-dark: #1f1f20;
    --brand-blue: #1b8fee;
    --ink: #2a2a2a;
    --ink-soft: #4a4a4a;
    --on-dark: #ffffff;
  }
  * { box-sizing: border-box; margin: 0; padding: 0; }
  html, body {
    width: 1200px; height: 1200px; overflow: hidden;
    background: var(--page-bg);
    font-family: "Montserrat", sans-serif;
  }
  .sheet {
    width: 1200px; height: 1200px;
    display: flex; flex-direction: column; align-items: center; justify-content: center;
    gap: 60px;
  }
  .card {
    position: relative;
    width: 860px; height: 491px;
    border-radius: 34px;
    overflow: hidden;
    box-shadow: 0 10px 30px rgba(0,0,0,.18);
  }
  /* Contact side */
  .card--contact { background: var(--card-white); }
  .contact {
    position: absolute; left: 96px; top: 150px;
  }
  .identity {
    border-left: 6px solid var(--brand-blue);
    padding-left: 16px;
    margin-bottom: 30px;
  }
  .identity__name {
    font-size: 44px; font-weight: 700; color: var(--brand-blue);
    letter-spacing: .5px; line-height: 1;
  }
  .identity__role {
    font-size: 19px; font-weight: 500; color: var(--ink-soft);
    margin-top: 6px; letter-spacing: .5px;
  }
  .details { list-style: none; }
  .details li {
    display: flex; align-items: center; gap: 16px;
    font-size: 22px; color: var(--ink); margin-bottom: 12px;
  }
  .details svg { width: 26px; height: 26px; flex: none; }
  .wordmark--small {
    position: absolute; right: 70px; top: 110px;
    display: flex; align-items: center; gap: 14px;
  }
  .wordmark__square {
    width: 30px; height: 30px; background: var(--brand-blue);
  }
  .wordmark__text {
    font-size: 30px; font-weight: 700; color: var(--ink);
    letter-spacing: 2px;
  }
  .accent-band {
    position: absolute; left: 410px; bottom: 0;
    width: 330px; height: 22px; background: var(--brand-blue);
  }
  /* Logo side */
  .card--logo {
    background: var(--card-dark);
    display: flex; align-items: center; justify-content: center;
  }
  .wordmark--large { display: flex; align-items: center; gap: 22px; }
  .wordmark--large .wordmark__square { width: 46px; height: 46px; }
  .wordmark--large .wordmark__text {
    color: var(--on-dark); font-size: 44px; letter-spacing: 3px;
  }
</style>
</head>
<body>
<main class="sheet">
  <section class="card card--contact" aria-label="Contact side">
    <div class="wordmark wordmark--small">
      <span class="wordmark__square"></span>
      <span class="wordmark__text">KESTO ROOFING &amp; SIDING</span>
    </div>
    <div class="contact">
      <div class="identity">
        <h1 class="identity__name">JOHN DOE</h1>
        <p class="identity__role">CEO | FOUNDER</p>
      </div>
      <ul class="details">
        <li>
          <svg viewBox="0 0 24 24" fill="none" stroke="var(--brand-blue)" stroke-width="2"><rect x="6" y="2" width="12" height="20" rx="2"/><line x1="11" y1="18" x2="13" y2="18"/></svg>
          403-386-2049
        </li>
        <li>
          <svg viewBox="0 0 24 24" fill="var(--brand-blue)"><path d="M6.6 10.8a15.1 15.1 0 0 0 6.6 6.6l2.2-2.2a1 1 0 0 1 1-.25 11.4 11.4 0 0 0 3.6.57 1 1 0 0 1 1 1V20a1 1 0 0 1-1 1A17 17 0 0 1 3 4a1 1 0 0 1 1-1h3.5a1 1 0 0 1 1 1c0 1.25.2 2.45.57 3.57a1 1 0 0 1-.25 1z"/></svg>
          403-386-2049
        </li>
        <li>
          <svg viewBox="0 0 24 24" fill="var(--brand-blue)"><path d="M2 5h20v14H2z"/><path d="M2 5l10 8 10-8" fill="none" stroke="#fff" stroke-width="1.6"/></svg>
          email@youremail.com
        </li>
        <li>
          <svg viewBox="0 0 24 24" fill="none" stroke="var(--brand-blue)" stroke-width="2"><circle cx="12" cy="12" r="10"/><ellipse cx="12" cy="12" rx="4.5" ry="10"/><line x1="2" y1="12" x2="22" y2="12"/></svg>
          prairieshinglepros.com
        </li>
      </ul>
    </div>
    <div class="accent-band"></div>
  </section>

  <section class="card card--logo" aria-label="Logo side">
    <div class="wordmark wordmark--large">
      <span class="wordmark__square"></span>
      <span class="wordmark__text">KESTO ROOFING &amp; SIDING</span>
    </div>
  </section>
</main>
</body>
</html>
```